Hi!
We need a cool brochure / leaflet for our Flenvo product line.
These are plastic corrugated sheets which are used to make various products.
When you look at the Flenvo section on our website: http://plandexo.com/flenvo/ you will get a bit more info (the website is under construction).
We need a separate page for a few products.
But for now we need just one test page for the first product group "Surface Protection". If your design is approved as a template, we will give you the text and pics for the other products. We can set a price per page for the other pages later.
Requirements:
- Size should be A4. The leaflet will be combined into one full brochure at the end. But each page will also need to function a a separate leaflet for that particular product. (For example it will also be placed on the website as a downloadable PDF)
- Font needs to be Gill Sans MT
- This is the brand logo: https://files.quorvault.net/s/k3p81wrd/Flenvo%20logo%20-%20registered.ai
- These 3 pics should be use on leaflet: https://files.quorvault.net/sh/m72tq9xz/BBdk4wLrTn
- Here you can find the text: https://files.quorvault.net/s/v9h2ya5e/Text%20-%20Surface%20Protection.docx
- The icons in this text part (including text) also need to be placed in the brochure. The originals can be found here: https://files.quorvault.net/sh/p4n6ub0c/CCfj8sXoWe
Please think outside of the box as much as possible.
And make sure to use mainly white and the "Flenvo logo" blue.
We also have another product group which will need to be done after this project.
Looking forward to your design!
Regards,
Jorn
Construction
Plastic

```html
<!DOCTYPE html>
<html lang="en">
<head>
<meta charset="utf-8">
<title>Flenvo Surface Protection Leaflet</title>
<link href="https://fonts.googleapis.com/css2?family=PT+Sans:wght@400;700&family=PT+Sans+Narrow:wght@400;700&display=swap" rel="stylesheet">
<style>
  :root {
    --sheet-blue: #3597c6;
    --sheet-blue-deep: #1f74a6;
    --sheet-blue-light: #5cb4dc;
    --leaf-green: #8cc63f;
    --icon-navy: #1d3c86;
    --ink-navy: #173a78;
    --white: #ffffff;
    --page-bg: #ffffff;
  }
  * { box-sizing: border-box; margin: 0; padding: 0; }
  html, body { width: 1200px; height: 1000px; overflow: hidden; background: var(--page-bg); }
  body { font-family: "PT Sans", sans-serif; color: var(--white); }
  .canvas { position: relative; width: 1200px; height: 1000px; overflow: hidden; }

  .spread {
    position: absolute; left: 0; width: 685px; height: 490px; overflow: hidden;
    background: linear-gradient(160deg, var(--sheet-blue-light) 0%, var(--sheet-blue) 45%, var(--sheet-blue-deep) 100%);
  }
  .spread--outer { top: 0; }
  .spread--inner { top: 510px; }

  .photo { position: absolute; z-index: 0; }
  .photo--cutter-outer {
    left: 150px; top: -10px; width: 330px; height: 470px;
    background: linear-gradient(150deg, rgba(40,70,170,0.85), rgba(25,45,130,0.6) 70%, rgba(200,210,220,0.4));
    clip-path: polygon(62% 0, 100% 6%, 45% 100%, 18% 96%);
  }
  .photo--cutter-inner {
    left: 0; top: 0; width: 230px; height: 210px;
    background: linear-gradient(150deg, rgba(40,70,170,0.85), rgba(25,45,130,0.55) 70%, rgba(200,210,220,0.35));
    clip-path: polygon(55% 0, 100% 0, 38% 100%, 18% 98%, 20% 40%);
  }
  .photo--sheets {
    left: 218px; top: 395px; width: 237px; height: 95px;
    background: linear-gradient(180deg, #8cc63f 0%, #d8dde2 30%, #ffffff 45%, #2a2a2a 65%, #5a7fc0 85%, #2f5fb0 100%);
  }
  .photo--worker {
    left: 585px; top: 230px; width: 100px; height: 260px;
    background: linear-gradient(200deg, rgba(233,238,242,0.55) 0%, rgba(240,122,42,0.75) 45%, #4a6f96 78%, #2f5f8f 100%);
    clip-path: polygon(40% 0, 100% 0, 100% 100%, 0 100%, 0 30%);
  }

  .panel-title {
    position: absolute; z-index: 1; font-weight: 700; font-size: 21px; color: var(--white);
    transform: rotate(-8deg); transform-origin: left bottom; white-space: nowrap;
  }

  .feature-list { position: absolute; left: 0; top: 131px; list-style: none; }
  .feature {
    position: relative; width: 210px; height: 24px; margin-bottom: 12px;
    background: var(--leaf-green); border-radius: 0 12px 12px 0;
    display: flex; align-items: center; padding-left: 65px;
    font-size: 15px; color: var(--white);
  }
  .feature .icon { position: absolute; left: 27px; top: -3px; }

  .icon {
    width: 30px; height: 30px; border-radius: 50%;
    background: var(--icon-navy); border: 2px solid var(--white);
    display: flex; align-items: center; justify-content: center;
  }
  .icon svg { width: 16px; height: 16px; }

  .brand { position: absolute; text-align: center; color: var(--white); }
  .brand-name { font-weight: 700; font-size: 30px; letter-spacing: 3px; line-height: 1; }
  .brand-tagline { font-size: 8px; letter-spacing: 0.5px; margin-top: 4px; }
  .brand-url { font-size: 5px; margin-top: 1px; }
  .company-info { position: absolute; left: 284px; top: 432px; font-family: "PT Sans Narrow", sans-serif; font-weight: 700; font-size: 12px; }

  .brand-backdrop {
    position: absolute; left: 450px; top: 60px; transform: rotate(13deg); transform-origin: left top;
    color: rgba(235,235,235,0.85); white-space: nowrap;
  }
  .brand-backdrop .brand-name { font-size: 58px; letter-spacing: 6px; }
  .brand-backdrop .brand-tagline { font-size: 15px; letter-spacing: 2px; margin-top: 6px; }
  .brand-backdrop .brand-url { font-size: 9px; letter-spacing: 1px; }

  .section-tag {
    position: absolute; left: 0; top: 206px; width: 182px; height: 22px;
    background: var(--leaf-green); border-radius: 0 11px 11px 0;
    font-weight: 700; font-size: 15px; padding-left: 25px; line-height: 22px;
  }
  .section-body {
    position: absolute; left: 25px; top: 230px; width: 190px;
    font-family: "PT Sans Narrow", sans-serif; font-weight: 700; font-size: 11.3px; line-height: 16.4px;
  }

  .spec-column {
    position: absolute; z-index: 1; width: 208px;
    display: flex; flex-direction: column; gap: 6px;
  }
  .spec-column--left { left: 232px; top: 68px; }
  .spec-column--right { left: 466px; top: 25px; }
  .spec-head {
    position: relative; height: 20px; background: var(--leaf-green); border-radius: 0 10px 10px 0;
    padding-left: 28px; line-height: 20px;
    font-family: "PT Sans Narrow", sans-serif; font-weight: 700; font-size: 12.5px; color: var(--ink-navy);
    white-space: nowrap;
  }
  .spec-head .icon { position: absolute; left: 0; top: -4px; width: 24px; height: 24px; border-width: 1.5px; }
  .spec-head .icon svg { width: 13px; height: 13px; }
  .spec-body {
    font-family: "PT Sans Narrow", sans-serif; font-size: 10.8px; line-height: 12.6px;
    color: var(--white); margin-top: 2px;
  }
</style>
</head>
<body>
<main class="canvas">

  <section class="spread spread--outer">
    <div class="photo photo--cutter-outer" role="img" aria-label="Blue utility knife cutting a corrugated plastic sheet"></div>

    <div class="brand-backdrop" aria-hidden="true">
      <div class="brand-name">FLENVO</div>
      <div class="brand-tagline">PLASTIC CORRUGATED SHEETS</div>
      <div class="brand-url">WWW.FLENVO.COM</div>
    </div>

    <h2 class="panel-title" style="left:40px; top:80px;">Flenvo Features:</h2>

    <ul class="feature-list">
      <li class="feature"><span class="icon"><svg viewBox="0 0 16 16"><text x="8" y="13" text-anchor="middle" font-size="14" font-weight="700" fill="#fff" font-family="PT Sans, sans-serif">$</text></svg></span>Cost Efficient</li>
      <li class="feature"><span class="icon"><svg viewBox="0 0 16 16"><path d="M3 13 L9 7 M8 4 L12 8 L10 10 L6 6 Z" stroke="#fff" stroke-width="1.6" fill="#fff"/></svg></span>Easy to Install</li>
      <li class="feature"><span class="icon"><svg viewBox="0 0 16 16"><path d="M3 12 Q5 4 11 5 Q9 8 12 10 Q8 13 3 12Z" stroke="#fff" stroke-width="1.3" fill="none"/></svg></span>Strong</li>
      <li class="feature"><span class="icon"><svg viewBox="0 0 16 16"><path d="M3 14 C5 8 9 4 13 2 C12 7 9 11 3 14Z" fill="#fff"/></svg></span>Light Weight</li>
      <li class="feature"><span class="icon"><svg viewBox="0 0 16 16"><rect x="2" y="10" width="12" height="3" fill="#fff"/><path d="M5 9 L8 3 L11 9Z" fill="#fff"/></svg></span>Shock Resistant</li>
      <li class="feature"><span class="icon"><svg viewBox="0 0 16 16"><circle cx="8" cy="8" r="6" stroke="#fff" stroke-width="1.6" fill="none"/><path d="M8 4 V8 L11 10" stroke="#fff" stroke-width="1.6" fill="none"/></svg></span>Time Saving</li>
      <li class="feature"><span class="icon"><svg viewBox="0 0 16 16"><path d="M8 2 C11 7 12 9 12 11 A4 4 0 0 1 4 11 C4 9 5 7 8 2Z" fill="#fff"/></svg></span>Waterproof</li>
    </ul>

    <div class="brand" style="left:266px; top:378px; width:170px;">
      <div class="brand-name">FLENVO</div>
      <div class="brand-tagline">PLASTIC CORRUGATED SHEETS</div>
      <div class="brand-url">WWW.FLENVO.COM</div>
    </div>
    <div class="company-info">WEBSITE/COMPANY INFO</div>

    <div class="brand" style="left:490px; top:338px; width:150px;">
      <div class="brand-name">FLENVO</div>
      <div class="brand-tagline">PLASTIC CORRUGATED SHEETS</div>
      <div class="brand-url">WWW.FLENVO.COM</div>
    </div>
  </section>

  <section class="spread spread--inner">
    <div class="photo photo--cutter-inner" role="img" aria-label="Blue utility knife with red button on a corrugated sheet"></div>
    <div class="photo photo--sheets" role="img" aria-label="Stack of coloured corrugated plastic sheets seen edge-on"></div>
    <div class="photo photo--worker" role="img" aria-label="Construction worker in hard hat and safety vest taping protective sheets to a floor"></div>

    <div class="section-tag">SURFACE PROTECTION</div>
    <p class="section-body">Flenvo sheets are used for temporary floor and wall protection. The plastic corrugated sheets are designed to provide reusable surface protection for many fixtures and surfaces during construction. The sheets offer excellent surface protection for surfaces like concrete, tile, vinyl, wooden floors, doors, counters, and cabinets. The sheets are easy to apply and cost-effective.<br>Flenvo sheets are similar to Corvexa sheets are also sold in by the name of PP hollow sheets, twinwall sheets, fluted boards and polypropylene corrugated sheets.</p>

    <h2 class="panel-title" style="left:232px; top:38px;">Flenvo Specifications:</h2>

    <div class="spec-column spec-column--left">
      <div class="spec">
        <div class="spec-head"><span class="icon"><svg viewBox="0 0 16 16"><path d="M8 2 V14 M5 4 H11 M5 12 H11" stroke="#fff" stroke-width="1.6"/></svg></span>Thickness</div>
        <p class="spec-body">Flenvo sheets can be produced in a thickness between 1.5 and 10 mm. We can advise you on what thickness to choose depending on the purpose of use.</p>
      </div>
      <div class="spec">
        <div class="spec-head"><span class="icon"><svg viewBox="0 0 16 16"><path d="M3 6 H13 M8 3 V13 M4 6 L2 10 H6Z M12 6 L10 10 H14Z" stroke="#fff" stroke-width="1.3" fill="none"/></svg></span>Weight</div>
        <p class="spec-body">The weight of Flenvo sheets is expressed in GSM (grams per square meter). The higher you choose your GSM, the stronger and stiffer the material will be.</p>
      </div>
      <div class="spec">
        <div class="spec-head"><span class="icon"><svg viewBox="0 0 16 16"><rect x="2" y="5" width="12" height="6" stroke="#fff" stroke-width="1.5" fill="none"/><path d="M5 5 V8 M8 5 V9 M11 5 V8" stroke="#fff" stroke-width="1.2"/></svg></span>Size</div>
        <p class="spec-body">Flenvo sheets are available in any requested size. The length can be as long as required; the width is limited to 240 cm.</p>
      </div>
      <div class="spec">
        <div class="spec-head"><span class="icon"><svg viewBox="0 0 16 16"><path d="M2 14 L8 3 M2 14 L11 5 M2 14 L13 8 M2 14 L14 12" stroke="#fff" stroke-width="1.5"/></svg></span>Color</div>
        <p class="spec-body">Our customers can choose any color for the sheets or artwork. Just ask us what you need, and we can provide you with a sample.</p>
      </div>
      <div class="spec">
        <div class="spec-head"><span class="icon"><svg viewBox="0 0 16 16"><path d="M6 2 H10 M7 2 V6 L3 13 H13 L9 6 V2" stroke="#fff" stroke-width="1.4" fill="none"/></svg></span>Virgin and Recycled Polypropylene</div>
        <p class="spec-body">We can use 100% virgin polypropylene to produce your sheets. Another option is to let us recycle up to 20% of our internally regenerated polypropylene.</p>
      </div>
    </div>

    <div class="spec-column spec-column--right">
      <div class="spec">
        <div class="spec-head"><span class="icon"><svg viewBox="0 0 16 16"><rect x="4" y="2" width="8" height="4" fill="#fff"/><rect x="2" y="6" width="12" height="5" stroke="#fff" stroke-width="1.4" fill="none"/><rect x="4" y="10" width="8" height="4" fill="#fff"/></svg></span>Custom Printing</div>
        <p class="spec-body">Flenvo sheets can be supplied with high-resolution, full-color printing. Send us your design, and we can directly print it onto the sheets in our factory.</p>
      </div>
      <div class="spec">
        <div class="spec-head"><span class="icon"><svg viewBox="0 0 16 16"><path d="M8 2 C11 6 12 8 12 10 A4 4 0 0 1 4 10 C4 8 6 7 6 5 C7 6 8 5 8 2Z" fill="#ff6b3a"/></svg></span>Fire-Retardant Sheets</div>
        <p class="spec-body">A fire-retardant version of Flenvo sheets is available. Please let us know the fire rating you require, and we are happy to produce them for you.</p>
      </div>
      <div class="spec">
        <div class="spec-head"><span class="icon"><svg viewBox="0 0 16 16"><path d="M4 12 L7 4 M7 12 L10 4 M10 12 L13 4 M2 13 H14" stroke="#fff" stroke-width="1.4"/></svg></span>Corona Treatment</div>
        <p class="spec-body">We give our customers the choice to print their own sheets. If you choose this option, will give the sheets a corona treatment to make sure that the sheets are well prepared for printing.</p>
      </div>
      <div class="spec">
        <div class="spec-head"><span class="icon"><svg viewBox="0 0 16 16"><circle cx="8" cy="8" r="3" fill="#fff"/><path d="M8 1 V3 M8 13 V15 M1 8 H3 M13 8 H15 M3 3 L4.5 4.5 M11.5 11.5 L13 13 M3 13 L4.5 11.5 M11.5 4.5 L13 3" stroke="#fff" stroke-width="1.3"/></svg></span>UV Protection</div>
        <p class="spec-body">Flenvo sheets can be produced with a<br>UV protectant. This can extend the<br>lifecycle of the sheets and their print work.</p>
      </div>
      <div class="spec">
        <div class="spec-head"><span class="icon"><svg viewBox="0 0 16 16"><path d="M3 13 L9 7 M8 3 L13 8 L11 9 L7 5Z" stroke="#fff" stroke-width="1.5" fill="#fff"/></svg></span>Puncture Resistance</div>
        <p class="spec-body">We can supply our Flenvo sheets in any<br>requested puncture resistance grade.<br>Just let us know the PR you require,<br>and we will supply the material<br>including a test report.</p>
      </div>
    </div>
  </section>

</main>
</body>
</html>
```